Self-Serve Brazilian Buffet and BBQ sold by the pound needs a business card

For CEO -Lucia Fernanda Matos Hale
Owner/President - Marcos Tiago Matos

Target Market(s)

Customers and

Industry/Entity Type

Business

Contact Information for Business Card

Lucia Fernanda Pinto Matos Hale
CEO of Vento Lume Grill
Brazilian BBQ Buffet sold by the pound

Requirements
Must have
• 5186 West Linden Blvd.
• Ste. K
• Arroyo Vale, CA 90417
• Phone : 555810-2947
• ventolumegrill@postrova.com

```html
<!DOCTYPE html>
<html lang="en">
<head>
<meta charset="utf-8">
<title>Vento Lume Grill – Business Card</title>
<link rel="stylesheet" href="https://fonts.googleapis.com/css2?family=Open+Sans:wght@400;600&display=swap">
<style>
  :root {
    --page-bg: #e9e6e1;
    --cream-light: #fbf0d2;
    --cream-dark: #efdcae;
    --navy: #0d3a4f;
    --gold: #ecc97c;
    --white: #ffffff;
  }
  html, body {
    margin: 0;
    padding: 0;
    width: 1200px;
    height: 900px;
    overflow: hidden;
    background: var(--page-bg);
    font-family: "Open Sans", Arial, sans-serif;
  }
  .canvas {
    position: relative;
    width: 1200px;
    height: 900px;
    display: flex;
    align-items: center;
    justify-content: center;
  }
  .card {
    position: relative;
    width: 1000px;
    height: 580px;
    border-radius: 44px;
    overflow: hidden;
    background: var(--navy);
    box-shadow: 0 10px 30px rgba(0,0,0,0.18);
  }
  .card-shape {
    position: absolute;
    inset: 0;
    width: 100%;
    height: 100%;
  }
  .brand {
    position: absolute;
    top: 96px;
    left: 0;
    right: 0;
    display: flex;
    align-items: center;
    justify-content: center;
    gap: 18px;
  }
  .brand-dot {
    width: 34px;
    height: 34px;
    border-radius: 50%;
    background: var(--navy);
  }
  .brand-name {
    font-size: 52px;
    font-weight: 600;
    color: var(--navy);
    letter-spacing: 0.5px;
  }
  .details {
    position: absolute;
    top: 292px;
    left: 0;
    right: 0;
    text-align: center;
    color: var(--white);
  }
  .holder-name {
    margin: 0;
    font-size: 40px;
    font-weight: 400;
    color: var(--gold);
    line-height: 1.2;
  }
  .holder-title {
    margin: 4px 0 0;
    font-size: 22px;
    font-weight: 600;
    line-height: 1.3;
  }
  .rule {
    width: 560px;
    height: 2px;
    margin: 8px auto 14px;
    background: linear-gradient(90deg, transparent, var(--gold) 30%, var(--gold) 70%, transparent);
  }
  .contact {
    list-style: none;
    margin: 0;
    padding: 0;
    font-size: 26px;
    line-height: 1.6;
  }
</style>
</head>
<body>
<main class="canvas">
  <article class="card">
    <svg class="card-shape" viewBox="0 0 1000 580" preserveAspectRatio="none" aria-hidden="true">
      <defs>
        <linearGradient id="creamFill" x1="0" y1="0" x2="1" y2="1">
          <stop offset="0" stop-color="#fbf0d2"/>
          <stop offset="1" stop-color="#efdcae"/>
        </linearGradient>
      </defs>
      <rect width="1000" height="580" fill="#0d3a4f"/>
      <path d="M0 0 H1000 V215 Q640 330 0 250 Z" fill="url(#creamFill)"/>
    </svg>

    <div class="brand">
      <span class="brand-dot"></span>
      <span class="brand-name">Vento Lume Grill</span>
    </div>

    <section class="details">
      <h1 class="holder-name">Lucia Fernanda Matos Hale</h1>
      <p class="holder-title">CEO of Vento Lume Grill Brazilian BBQ Buffet sold by the pound</p>
      <div class="rule"></div>
      <ul class="contact">
        <li class="contact-phone">555810-2947</li>
        <li class="contact-email">ventolumegrill@postrova.com</li>
        <li class="contact-address">5186 West Linden Blvd. Ste. K, Arroyo Vale, CA 90417</li>
      </ul>
    </section>
  </article>
</main>
</body>
</html>
```